brightquokka.net we need a webpage designed for our new product

We need a webpage designed for our new range of products from our new brand. We have had a logo designed on sketchhive (see attached) and we want to keep to this theme. Our first product is a range of affordable app controlled LED lightbulbs.

I have added some photos that we think is good inspirational material and would be good as a background to this website, but we want the site to look modern but not conventional. We would like something that makes our company look quirky not corporate.

Thats it

Target Market(s)

Our product is being stocked by big name online retailers in the UK, the page will get link through hits from our app. Our target market is gadget freaks of all ages.

Industry/Entity Type

It Company

Requirements
Must have
• We are going to need a help page, text to be uploaded next few days.

We need a contact page.

design my work on iOS and Android as most people will access page through their handset or tablet.
Should not have
• We do not want anything too corporate.

```html
<!DOCTYPE html>
<html lang="en">
<head>
<meta charset="utf-8">
<title>Bright Quokka – App Controlled LED Lightbulbs</title>
<link rel="stylesheet" href="https://fonts.googleapis.com/css2?family=Aldrich&family=Lato:wght@400;700&display=swap">
<style>
:root{
  --green:#3aa935;
  --green-light:#a8e23c;
  --green-mid:#6cc13a;
  --text-dark:#3a3a3a;
  --text-grey:#8a8a8a;
  --band-dark:#3b3a36;
  --white:#ffffff;
}
*{margin:0;padding:0;box-sizing:border-box}
html,body{width:1200px;height:1196px;overflow:hidden;background:var(--white)}
body{position:relative;font-family:"Lato",sans-serif;color:var(--text-dark)}

.site-header{position:absolute;left:0;top:0;width:1200px;height:63px}
.brand{position:absolute;left:180px;top:19px;font-family:"Aldrich",sans-serif;font-size:23px;color:var(--green);letter-spacing:1.5px}
.main-nav{position:absolute;left:486px;top:18px;display:flex}
.main-nav a{font-family:"Aldrich",sans-serif;font-size:12px;color:#555;text-decoration:none;letter-spacing:1px;height:28px;line-height:27px;text-align:center}
.main-nav a.active{border:1px solid #999;color:#222;width:79px}
.nav-new{width:83px}.nav-toys{width:82px}.nav-gadgets{width:96px}.nav-about{width:126px}.nav-contact{width:86px}

.hero{position:absolute;left:0;top:63px;width:1200px;height:283px;background:linear-gradient(100deg,#5fae4c 0%,#73bd5d 45%,#5aa84a 100%)}
.hero-products{position:absolute;left:630px;top:90px;width:380px;height:345px;border-radius:14px;background:radial-gradient(ellipse at 40% 70%,#f2f2f2 0%,#d6d6d6 45%,#2b2b2b 75%,#1e1e1e 100%)}
.hero-kicker{position:absolute;left:198px;top:178px;font-family:"Aldrich",sans-serif;font-size:17.5px;color:var(--white);letter-spacing:.6px;white-space:nowrap}
.hero-title{position:absolute;left:196px;top:200px;font-family:"Aldrich",sans-serif;font-size:38px;color:var(--white);letter-spacing:1px;white-space:nowrap}
.slide-arrow{position:absolute;top:185px;width:44px;height:42px;background:rgba(255,255,255,.55)}
.slide-arrow.prev{left:122px}.slide-arrow.next{left:1029px}
.slide-arrow svg{position:absolute;left:12px;top:11px}
.slide-dots{position:absolute;left:196px;top:370px;display:flex;gap:11px}
.slide-dots span{width:18px;height:18px;border-radius:50%;border:1.5px solid #666}
.slide-dots span.on{background:var(--green);border-color:var(--green)}

.welcome{position:absolute;left:190px;top:421px;width:820px}
.welcome h1{font-family:"Aldrich",sans-serif;font-weight:400;font-size:28px;color:#555;letter-spacing:1px;white-space:nowrap}
.welcome p{margin-top:13px;font-size:14px;line-height:18.2px;color:var(--text-grey)}

.features{position:absolute;left:0;top:595px;width:1200px;height:315px;background:linear-gradient(90deg,#4a4740 0%,#3b3a35 50%,#4d4b44 100%)}
.feature{position:absolute;top:58px;width:200px;height:200px;border-radius:50%;text-align:center;color:var(--white)}
.feature h2{font-family:"Aldrich",sans-serif;font-weight:400;font-size:29px;margin-top:68px;letter-spacing:1px}
.feature p{font-size:14px;line-height:17px;margin-top:10px}
.feature-shop{left:213px;background:radial-gradient(circle at 40% 40%,#5fcb45,#3aa935)}
.feature-blog{left:495px;background:radial-gradient(circle at 40% 40%,#b8f24a,#a0e030);color:#2f3a1a}
.feature-new{left:776px;background:radial-gradient(circle at 40% 40%,#86cc3c,#6cb52e)}

.site-footer{position:absolute;left:0;top:910px;width:1200px;height:286px}
.footer-heading{position:absolute;font-family:"Aldrich",sans-serif;font-size:21px;color:#333;letter-spacing:1px;white-space:nowrap}
.contact-heading{left:216px;top:48px}
.hours-heading{left:804px;top:48px}
.contact-icon{position:absolute}
.contact-phone{position:absolute;left:278px;top:98px;font-family:"Aldrich",sans-serif;font-size:19px;color:#444;letter-spacing:1px;white-space:nowrap}
.contact-email{position:absolute;left:279px;top:124px;font-family:"Aldrich",sans-serif;font-size:12.5px;color:#666}
.contact-address{position:absolute;left:278px;top:166px;font-family:"Aldrich",sans-serif;font-size:12px;color:#777;line-height:20px;letter-spacing:.5px}
.contact-address strong{font-weight:400;font-size:15px;color:#444;margin-left:6px}
.footer-brand{position:absolute;left:0;width:1218px;top:231px;text-align:center;font-family:"Aldrich",sans-serif;font-size:13px;color:var(--green)}
.copyright{position:absolute;left:0;width:1218px;top:253px;text-align:center;font-size:11px;color:#555}
.hours{position:absolute;left:805px;font-family:"Aldrich",sans-serif;font-size:17px;letter-spacing:1px;line-height:21px;white-space:nowrap}
.hours .day{color:var(--green)}
.hours .time{color:#444}
.hours-week{top:100px}.hours-fri{top:167px}
</style>
</head>
<body>
<header class="site-header">
  <div class="brand">BRIGHTQUOKKA</div>
  <nav class="main-nav">
    <a class="active" href="#">HOME</a>
    <a class="nav-new" href="#">NEW</a>
    <a class="nav-toys" href="#">TOYS</a>
    <a class="nav-gadgets" href="#">GADGETS</a>
    <a class="nav-about" href="#">ABOUT US</a>
    <a class="nav-contact" href="#">CONTACT</a>
  </nav>
</header>

<section class="hero" role="img" aria-label="Green painted texture background"></section>
<div class="hero-products" role="img" aria-label="LED lightbulbs, remote, hub, tablet and phones running the lighting app"></div>
<div class="hero-kicker">Huge range of affordable app controlled</div>
<div class="hero-title">LED lightbulbs</div>
<div class="slide-arrow prev"><svg width="20" height="20" viewBox="0 0 20 20"><path d="M13 2 L5 10 L13 18" fill="none" stroke="#3aa935" stroke-width="2"/></svg></div>
<div class="slide-arrow next"><svg width="20" height="20" viewBox="0 0 20 20"><path d="M7 2 L15 10 L7 18" fill="none" stroke="#3aa935" stroke-width="2"/></svg></div>
<div class="slide-dots"><span></span><span class="on"></span><span></span><span></span></div>

<section class="welcome">
  <h1>Welcome to Bright Quokka</h1>
  <p>Duis autem vel eum iriure dolor in hendrerit in vulputate velit esse molestie consequat, vel illum dolore eu feugiat nulla facilisis at vero eros et accumsan. Duis autem vel eum iriure dolor in hendrerit in vulputate velit esse molestie consequat, vel illum dolore eu feugiat nulla facilisis at vero eros et accumsan.Lorem ipsum dolor sit amet, consectetuer adipiscing elit, sed diam nonummy nibh euismod tincidunt ut laoreet.Vulputate velit esse molestie consequat, vel illum dolore eu feugiat nulla facilisis at vero eros et accumsan.Lorem ipsum dolor sit amet, consectetuer adipiscing elit, sed diam nonummy nibh euismod tincidunt ut laoreet...</p>
</section>

<section class="features" role="img" aria-label="Dimmed photo of a toy and gadget shop interior">
  <div class="feature feature-shop"><h2>Our Shop</h2><p>Let's Visit our Shop<br>Online!</p></div>
  <div class="feature feature-blog"><h2>Blog</h2><p>What our Customers<br>talk about us!</p></div>
  <div class="feature feature-new"><h2>New</h2><p>Check out what's<br>new in Stock</p></div>
</section>

<footer class="site-footer">
  <div class="footer-heading contact-heading">Contact us</div>
  <svg class="contact-icon" style="left:216px;top:100px" width="44" height="40" viewBox="0 0 44 40" fill="none" stroke="#3aa935" stroke-width="2.5">
    <rect x="2" y="2" width="40" height="36"/>
    <circle cx="15" cy="15" r="4"/>
    <path d="M8 30 Q8 22 15 22 Q22 22 22 30"/>
    <path d="M26 13 H36 M26 20 H36"/>
  </svg>
  <div class="contact-phone">Tlf. 00 47 00 31</div>
  <div class="contact-email">info@brightquokka.net</div>
  <svg class="contact-icon" style="left:222px;top:172px" width="30" height="46" viewBox="0 0 30 46" fill="none" stroke="#3aa935" stroke-width="2.5">
    <path d="M15 34 C8 24 4 18 4 13 A11 11 0 0 1 26 13 C26 18 22 24 15 34 Z" fill="#3aa935"/>
    <circle cx="15" cy="13" r="4" fill="#fff" stroke="none"/>
    <ellipse cx="15" cy="40" rx="12" ry="4"/>
  </svg>
  <div class="contact-address"><strong>Bright Quokka</strong><br>ABC, London<br>United Kingdom.</div>

  <div class="footer-brand">BRIGHTQUOKKA</div>
  <div class="copyright">© 2014 BRIGHT QUOKKA &nbsp;|&nbsp; ALL RIGHTS RESERVED</div>

  <div class="footer-heading hours-heading">Opening hours</div>
  <div class="hours hours-week"><div class="day">MON - THURS.</div><div class="time">8:00 &nbsp;- &nbsp;17:00</div></div>
  <div class="hours hours-fri"><div class="day">FRI</div><div class="time">8:00 &nbsp;- &nbsp;14:00</div></div>
</footer>
</body>
</html>
```